Meridale Wall Tracking Office

I have a current web site that it looking quite aged and it needs a new lease of life. This is a Graffiti Management Website so is all about data processing and management of information. I want a html 5 view on any platform design. clean crisp and new. I have provided some screen shots of my current site.

Target Market(s)

The Target Market will be local government. most users will not be heavy pc users

Industry/Entity Type

Management

Font styles to use
Sans Serif
Other font styles liked:
• web font like calibri

Colors

Designer to choose colors to be used in the design.

Requirements
Must have
• Must have menus similar to attachments

```html
<!DOCTYPE html>
<html lang="en">
<head>
<meta charset="utf-8">
<title>MWTO – Graffiti Photo Maintenance</title>
<link href="https://fonts.googleapis.com/css2?family=Open+Sans:wght@400;600;700&display=swap" rel="stylesheet">
<style>
:root{
  --page-bg:#eef0f1;
  --navy:#152a45;
  --sky:#5699d6;
  --sky-deep:#3469a2;
  --sky-line:#4e8fcc;
  --admin-bg:#3469a2;
  --white:#ffffff;
  --ink:#333333;
  --muted:#555555;
  --link:#3d8fdb;
  --rule:#e3e3e3;
  --band:#ececec;
  --field-border:#bdbdbd;
  --btn-grey:#f1f1f1;
  --green:#3db424;
  --green-edge:#2f9a1a;
  --rust:#c4450e;
  --ok:#5a9ad8;
  --footer-text:#6fa2d6;
}
*{box-sizing:border-box;margin:0;padding:0}
html,body{width:1200px;height:855px;overflow:hidden}
body{background:var(--page-bg);font-family:"Open Sans",Arial,sans-serif;color:var(--ink);position:relative}
.page{position:absolute;left:115px;top:0;width:971px;height:855px;background:var(--white)}
.topbar{position:absolute;left:0;top:0;width:971px;height:35px;background:var(--navy);color:var(--sky);font-size:10.5px;letter-spacing:1.2px;text-transform:uppercase}
.topbar .tagline{position:absolute;left:25px;top:10px}
.topbar .logout{position:absolute;right:24px;top:10px;font-weight:700;font-size:11px;letter-spacing:.3px;display:flex;align-items:center;gap:8px;color:#7fb1e2}
.masthead{position:absolute;left:0;top:35px;width:971px;height:103px;
  background:repeating-linear-gradient(180deg,var(--sky) 0 5px,var(--sky-line) 5px 6px)}
.brand{position:absolute;left:0;right:0;top:20px;text-align:center;font-weight:700;font-size:52px;color:var(--white);letter-spacing:6px;line-height:60px}
.subband{position:absolute;left:0;top:138px;width:971px;height:30px;background:var(--sky-deep);color:var(--white);text-align:center;font-weight:700;font-size:11px;letter-spacing:1.6px;line-height:30px}
.sidebar{position:absolute;left:0;top:168px;width:230px;height:621px;background:var(--sky)}
.nav-home{height:54px;background:var(--white);display:flex;align-items:center;padding-left:24px;color:var(--link);font-weight:600;font-size:12px;position:relative}
.nav-home .chev{position:absolute;right:12px;top:19px}
.nav-item{height:46.5px;border-bottom:1px solid #4a88c5;display:flex;align-items:center;padding-left:22px;color:var(--white);font-weight:600;font-size:12px;text-transform:uppercase}
.nav-item svg,.nav-home svg{width:22px;height:20px;margin-right:22px;flex:none}
.nav-item.active{background:var(--admin-bg);font-weight:700;height:49px;border:0}
.groupbar{position:absolute;left:230px;top:168px;width:741px;height:55px;border-bottom:2px solid var(--rule);font-size:14px;padding:18px 0 0 22px}
.groupbar .group-name{color:var(--link);font-weight:600;margin-left:4px}
.panel{position:absolute;left:230px;top:223px;width:741px;height:566px;border-left:6px solid var(--rule)}
.panel-title{position:absolute;left:13px;top:16px;font-size:15px;font-weight:600;color:#2e2e2e}
.panel-rule{position:absolute;left:6px;right:13px;top:51px;border-top:1px solid var(--rule)}
.gallery-label{position:absolute;left:0;right:0;top:74px;text-align:center;color:var(--link);font-size:13.5px;font-weight:600}
.gallery{position:absolute;left:0;top:113px;width:735px;height:120px}
.arrow{position:absolute;top:30px}
.thumb{position:absolute;top:0;width:97px}
.thumb .shot{width:97px;height:78px}
.thumb .cap{font-size:12.5px;text-align:center;margin-top:7px;color:#333}
.slot{position:absolute;top:0;width:101px;height:81px;border:1px solid #e2e2e2;background:#f9f9f9;display:flex;align-items:center;justify-content:center}
.slot span{width:19px;height:19px;background:var(--sky);border-radius:2px;display:flex;align-items:center;justify-content:center}
.shot-a{background:linear-gradient(160deg,#6d6656,#8d8470 45%,#5b5a4d)}
.shot-b{background:linear-gradient(160deg,#5c6152,#9a9a90 50%,#4d5145)}
.shot-c{background:linear-gradient(180deg,#6c6a62,#8b8a83 55%,#c9c7c1)}
.format-band{position:absolute;left:0;top:252px;width:735px;height:41px;background:var(--band);border-top:1px solid #d6d6d6;text-align:center;font-size:12.5px;line-height:40px;color:#444}
.form-row{position:absolute;left:0;width:735px;height:36px}
.form-row label{position:absolute;left:29px;top:9px;font-size:14px;color:#333}
.field{position:absolute;left:172px;top:0;width:285px;height:35px;border:1px solid var(--field-border);border-radius:3px;background:#fff}
.btn{position:absolute;top:0;height:35px;border-radius:2px;font-family:inherit;font-size:14px;display:flex;align-items:center;justify-content:center;gap:8px}
.btn-browse{left:465px;width:104px;background:var(--btn-grey);border:1px solid var(--field-border);color:#333}
.btn-save{left:600px;width:104px;background:var(--green);border:1px solid var(--green-edge);color:#fff}
.btn-delete{left:465px;width:104px;background:var(--rust);border:1px solid #a73a0c;color:#fff}
.btn-ok{position:absolute;left:311px;top:492px;width:111px;height:34px;background:var(--ok);color:#fff;font-size:15px;font-weight:600;display:flex;align-items:center;justify-content:center;border-radius:2px}
.footer{position:absolute;left:0;top:789px;width:971px;height:66px;background:var(--navy);border-top:2px solid #1d2f8a}
.footer .copy{position:absolute;left:31px;top:25px;font-size:13px;color:var(--footer-text)}
.footer .social{position:absolute;right:22px;top:24px;display:flex;gap:7px}
.footer .social i{width:21px;height:21px;border-radius:50%;background:#4a7fc0;display:block}
</style>
</head>
<body>
<div class="page">
  <div class="topbar">
    <span class="tagline">Helping you clean up your community</span>
    <span class="logout">
      <svg width="15" height="15" viewBox="0 0 16 16"><path d="M5 3.5A6 6 0 1 0 11 3.5" fill="none" stroke="#7fb1e2" stroke-width="2"/><path d="M8 1v7" stroke="#7fb1e2" stroke-width="2"/></svg>LOGOUT
    </span>
  </div>
  <header class="masthead"><div class="brand">MWTO</div></header>
  <div class="subband">MERIDALE WALL TRACKING OFFICE</div>

  <nav class="sidebar">
    <div class="nav-home">
      <svg viewBox="0 0 20 20"><path d="M10 2 1 10h3v8h4v-5h4v5h4v-8h3z" fill="var(--sky-deep)"/></svg>USER HOME
      <svg class="chev" width="10" height="16" viewBox="0 0 10 16"><path d="M2 1l6 7-6 7" fill="none" stroke="#999" stroke-width="1.4"/></svg>
    </div>
    <div class="nav-item"><svg viewBox="0 0 24 20"><rect x="1" y="5" width="17" height="12" rx="2" fill="#dbe9f7"/><rect x="6" y="2" width="7" height="4" fill="none" stroke="#dbe9f7" stroke-width="1.5"/><circle cx="19" cy="15" r="4.5" fill="#dbe9f7"/><path d="M19 12.5v5M16.5 15h5" stroke="var(--sky)" stroke-width="1.6"/></svg>Add a Job</div>
    <div class="nav-item"><svg viewBox="0 0 24 20"><path d="M10 1h4l-1 3 2 12-3 3-3-3 2-12z" fill="#dbe9f7"/></svg>Current Jobs</div>
    <div class="nav-item"><svg viewBox="0 0 24 20"><rect x="1" y="5" width="17" height="12" rx="2" fill="#dbe9f7"/><rect x="6" y="2" width="7" height="4" fill="none" stroke="#dbe9f7" stroke-width="1.5"/><circle cx="19" cy="15" r="4.5" fill="#dbe9f7"/><path d="M17.3 13.3l3.4 3.4M20.7 13.3l-3.4 3.4" stroke="var(--sky)" stroke-width="1.5"/></svg>Closed Jobs</div>
    <div class="nav-item"><svg viewBox="0 0 24 20"><circle cx="9" cy="8" r="6" fill="none" stroke="#dbe9f7" stroke-width="2.4"/><path d="M13.5 12.5l6 6" stroke="#dbe9f7" stroke-width="3"/></svg>Search Jobs</div>
    <div class="nav-item"><svg viewBox="0 0 24 20"><path d="M10 2a8 8 0 1 0 8 8h-8z" fill="#dbe9f7"/><path d="M12 0v8h8a8 8 0 0 0-8-8z" fill="#dbe9f7"/></svg>Reports</div>
    <div class="nav-item"><svg viewBox="0 0 24 20"><circle cx="11" cy="10" r="9.5" fill="#dbe9f7"/><circle cx="11" cy="7.5" r="3.5" fill="var(--sky)"/><path d="M4.5 16.5a7 5 0 0 1 13 0" fill="var(--sky)"/></svg>User Details</div>
    <div class="nav-item active"><svg viewBox="0 0 24 20"><circle cx="11" cy="10" r="6" fill="none" stroke="#fff" stroke-width="3.5" stroke-dasharray="3 1.7"/><circle cx="11" cy="10" r="4.5" fill="none" stroke="#fff" stroke-width="2"/></svg>Admin</div>
  </nav>

  <div class="groupbar">Group Selected : <span class="group-name">Kestrel Bay Shire Council</span></div>

  <main class="panel">
    <h1 class="panel-title">GRAFFITI PHOTO MAINTAINANCE</h1>
    <div class="panel-rule"></div>
    <div class="gallery-label">Cleaned Photos</div>
    <div class="gallery">
      <svg class="arrow" style="left:20px" width="12" height="18" viewBox="0 0 12 18"><path d="M10 2 3 9l7 7" fill="none" stroke="#ccc" stroke-width="2.2"/></svg>
      <div class="thumb" style="left:55px"><div class="shot shot-a" role="img" aria-label="Cleaned wall photo 1"></div><div class="cap">11865 - 1.jpg</div></div>
      <div class="thumb" style="left:182px"><div class="shot shot-b" role="img" aria-label="Cleaned wall photo 2"></div><div class="cap">11865 - 2.jpg</div></div>
      <div class="thumb" style="left:312px"><div class="shot shot-c" role="img" aria-label="Cleaned wall photo 3"></div><div class="cap">11865 - 3.jpg</div></div>
      <div class="slot" style="left:436px"><span><svg width="11" height="11" viewBox="0 0 11 11"><path d="M5.5 1v9M1 5.5h9" stroke="#fff" stroke-width="2"/></svg></span></div>
      <div class="slot" style="left:562px"><span><svg width="11" height="11" viewBox="0 0 11 11"><path d="M5.5 1v9M1 5.5h9" stroke="#fff" stroke-width="2"/></svg></span></div>
      <svg class="arrow" style="left:704px" width="12" height="18" viewBox="0 0 12 18"><path d="M2 2l7 7-7 7" fill="none" stroke="#333" stroke-width="2.4"/></svg>
    </div>
    <div class="format-band">Photo Format to be “ JPEG ” &amp; size not to exceed 500k</div>

    <div class="form-row" style="top:330px">
      <label>Add Graffiti Photo</label><div class="field"></div>
      <div class="btn btn-browse">Browse...</div>
      <div class="btn btn-save"><svg width="14" height="14" viewBox="0 0 14 14"><path d="M1 1h10l2 2v10H1z" fill="none" stroke="#fff" stroke-width="1.6"/><rect x="4" y="1" width="5" height="4" fill="#fff"/><rect x="3.5" y="8" width="7" height="4" fill="#fff"/></svg>Save</div>
    </div>
    <div class="form-row" style="top:380px">
      <label>Add Cleaned Photo</label><div class="field"></div>
      <div class="btn btn-browse">Browse...</div>
      <div class="btn btn-save"><svg width="14" height="14" viewBox="0 0 14 14"><path d="M1 1h10l2 2v10H1z" fill="none" stroke="#fff" stroke-width="1.6"/><rect x="4" y="1" width="5" height="4" fill="#fff"/><rect x="3.5" y="8" width="7" height="4" fill="#fff"/></svg>Save</div>
    </div>
    <div class="form-row" style="top:429px">
      <label>Delete Photo Name</label><div class="field"></div>
      <div class="btn btn-delete"><svg width="12" height="14" viewBox="0 0 12 14"><rect x="0" y="1.5" width="12" height="2" fill="#fff"/><rect x="4" y="0" width="4" height="2" fill="#fff"/><path d="M1.5 4.5h9l-1 9.5h-7z" fill="#fff"/></svg>Delete</div>
    </div>
    <div class="btn-ok">OK</div>
  </main>

  <footer class="footer">
    <div class="copy">copyright 2014 MWTO. All rights reserved</div>
    <div class="social"><i></i><i></i></div>
  </footer>
</div>
</body>
</html>
```